Modern and appealing business Wordpress site

I've been operating my consulting firm for 5 years and feel like it is time to really improve on my web presence as I'm starting to get more national attention. I had a logo made through this service a couple of years ago, and would like to get a website that matches the look of it. The website will be used to (1) advertise my services (2) provide a brief overview of our management philosophies, and (3) host a resource library database. I understand HTML, but am not as familiar with how to code Wordpress, so I need someone that can help upload themes.

The website can be found at www.trelmondgroup.com.

For design, I prefer round designs to square and want the color scheme to match the attached logo. I have included both the full logo and the abbreviated one.

I also have a new picture for CFO uploaded. I plan on getting a new one for the CEO in the coming weeks, so I would like someone that I could get to help make the modification at a later time.

The resource database will be put into a document library (probably Kiln7) once the final design is completed rather than having multiple pages with links...just so you know the final vision for the site.

Reach out if you have any questions.

Target Market(s)

Community Action Agencies, Nonprofit Organization Leaders

Industry/Entity Type

Consulting

Coding

Coded - Design and coding required

Font styles to use
Sans Serif

Requirements
Must have
• Must match the color scheme of the attached logo

```html
<!DOCTYPE html>
<html lang="en">
<head>
<meta charset="utf-8">
<title>Trelmond Group, LLC</title>
<link href="https://fonts.googleapis.com/css2?family=Poppins:ital,wght@0,400;0,500;0,600;0,700;0,800;1,400&display=swap" rel="stylesheet">
<style>
:root{
  --blue:#2a9fd8;
  --blue-dark:#1c86c4;
  --ink:#3b3d42;
  --dark:#2b2c30;
  --text:#333;
  --muted:#666;
  --light:#eef2f6;
  --white:#fff;
}
*{margin:0;padding:0;box-sizing:border-box}
html,body{width:1200px;height:4317px;overflow:hidden}
body{font-family:"Poppins",sans-serif;color:var(--text);background:var(--white);position:relative}
.abs{position:absolute}
a{color:inherit;text-decoration:none}

/* top bar */
.topbar{position:absolute;left:0;top:0;width:1200px;height:53px;background:var(--dark);color:#fff;font-size:14px}
.topbar .item{position:absolute;top:17px;display:flex;align-items:center;gap:8px}
.topbar b{font-weight:600}
.topbar .sep{position:absolute;left:543px;top:14px;width:1px;height:24px;background:#888}
.social{display:flex;gap:10px}
.social span{width:38px;height:38px;border-radius:50%;border:2px solid var(--blue);display:block}
.topbar .social{position:absolute;left:920px;top:8px}

/* nav */
.nav{position:absolute;left:0;top:53px;width:1200px;height:98px;background:#fff}
.brand{display:flex;align-items:center;gap:10px;font-weight:700;color:var(--blue);font-size:34px;letter-spacing:1px}
.brand i{width:44px;height:44px;border-radius:50%;background:var(--blue);display:block}
.nav .brand{position:absolute;left:92px;top:26px}
.menu{position:absolute;left:484px;top:40px;display:flex;gap:36px;font-size:14px;font-weight:500;color:#333}
.menu .on{color:var(--blue);position:relative}
.menu .on:before{content:"";position:absolute;left:50%;top:-18px;width:14px;height:14px;margin-left:-7px;border-radius:50%;background:var(--blue)}
.btn-contact{position:absolute;left:958px;top:25px;width:148px;height:44px;border-radius:22px;background:var(--blue);color:#fff;font-weight:600;font-size:15px;display:flex;align-items:center;justify-content:center}

/* hero */
.hero{position:absolute;left:0;top:151px;width:1200px;height:637px;background:#2e2f33;overflow:hidden}
.hero-photo{position:absolute;left:561px;top:0;width:639px;height:560px;background:radial-gradient(circle at 55% 45%,#77746f,#4a4744 55%,#2e2f33 85%)}
.hero h1{position:absolute;left:92px;top:165px;color:#fff;font-weight:800;font-size:52px;line-height:62px;letter-spacing:.5px}
.hero h1 em{font-style:normal;color:var(--blue)}
.hero p{position:absolute;left:92px;top:296px;width:460px;color:#fff;font-size:17px;line-height:30px}
.btn-ghost{position:absolute;left:92px;top:379px;width:206px;height:52px;border-radius:26px;background:rgba(255,255,255,.2);color:#fff;font-weight:600;font-size:16px;display:flex;align-items:center;justify-content:center;gap:12px}
.dot-ico{width:22px;height:22px;border-radius:50%;background:currentColor;display:inline-block;opacity:.9}
.hero .wave{position:absolute;left:0;bottom:0}
.arrow{position:absolute;top:240px}

/* about */
.about-img{position:absolute;left:92px;top:878px;width:453px;height:454px;border-radius:70px 0 70px 0;background:linear-gradient(135deg,#d8d6d2,#a9a49b 55%,#5a4e80);border-bottom:8px solid var(--blue)}
.dots{position:absolute;background:rgba(60,60,60,.12)}
.h2{font-weight:800;font-size:40px;line-height:50px;color:#3c3e43}
.h2 em{font-style:normal;color:var(--blue)}
.about .h2{position:absolute;left:600px;top:918px}
.about p{position:absolute;left:600px;top:1078px;width:510px;font-size:16px;line-height:31px;color:#333}

/* services */
.services{position:absolute;left:0;top:1418px;width:1200px;height:794px;background:linear-gradient(135deg,#43ade0,#2494d2 60%,#3aa5dc)}
.services .title{position:absolute;left:0;top:68px;width:1200px;text-align:center;color:#fff;font-weight:800;font-size:40px}
.center-ico{position:absolute;left:578px;width:44px;height:30px;border-radius:50%;background:#fff}
.card{position:absolute;top:214px;width:240px;height:404px;background:#fff;text-align:center;clip-path:polygon(0 0,100% 0,100% 86%,50% 100%,0 86%);border-radius:26px 26px 0 0}
.card.dark{background:#3b3d42;color:#fff}
.card .ph{height:149px;border-radius:26px 26px 0 0}
.card h3{font-size:20px;font-weight:700;margin:16px 0 22px}
.card ul{list-style:none;padding:0 24px;font-size:15px;line-height:26px}
.card li{padding:8px 0 10px}
.card li+li{border-top:1px solid #ddd}
.card.dark li+li{border-top-color:#666}
.btn-white{position:absolute;left:478px;top:669px;width:246px;height:50px;border-radius:25px;background:#fff;color:#333;font-weight:600;font-size:15px;display:flex;align-items:center;justify-content:center;gap:12px}
.btn-white .dot-ico{color:var(--blue)}

/* mission */
.mission{position:absolute;left:0;top:2212px;width:1200px;height:553px;background:var(--light)}
.mission .h2{position:absolute;left:92px;top:178px;display:flex;align-items:center;gap:10px}
.mission p{position:absolute;left:92px;top:240px;width:360px;font-size:16px;line-height:31px}
.person{position:absolute;top:81px;width:270px;height:307px}
.person.ceo{left:525px;border-radius:0 0 60px 0;background:linear-gradient(160deg,#6b6f78,#2a3448 70%)}
.person.cfo{left:815px;border-radius:60px 0 0 0;background:linear-gradient(160deg,#7e6a58,#c9b8a6 50%,#2fa34b 95%)}
.caption{position:absolute;top:424px;width:270px;text-align:center}
.caption b{display:block;font-size:19px;font-weight:700}
.caption span{font-size:16px;color:#333}

/* testimonials */
.testi-title{position:absolute;left:0;top:2830px;width:1200px;text-align:center}
.tcard{position:absolute;top:2982px;width:485px;height:313px;background:var(--light);border-right:3px solid var(--blue);border-bottom:3px solid var(--blue);border-radius:0 0 14px 14px;text-align:center;padding:26px 26px 0}
.tcard .q{font-size:90px;font-weight:800;color:var(--blue);line-height:70px;height:60px}
.tcard p{font-style:italic;font-size:15.5px;line-height:31px;color:#333;margin-top:12px}
.tcard b{display:block;font-weight:600;font-size:15.5px;line-height:26px;margin-top:12px}
.pager{position:absolute;left:576px;top:3336px;display:flex;gap:7px}
.pager i{width:12px;height:12px;border-radius:50%;background:var(--blue);display:block}
.pager i.on{background:#444}

/* contact */
.touch{position:absolute;left:0;top:3402px;width:590px;height:545px;background:linear-gradient(135deg,#3b3a38,#26272a 60%,#3f3d39)}
.touch h2{position:absolute;left:92px;top:64px;color:#fff;font-weight:800;font-size:38px;display:flex;align-items:center;gap:10px}
.touch p{position:absolute;left:92px;top:136px;width:430px;color:#fff;font-style:italic;font-size:16px;line-height:31px}
.touch .info{position:absolute;left:92px;color:#fff;font-size:15px;display:flex;align-items:flex-start;gap:14px;line-height:22px}
.touch .info .bar{width:3px;height:40px;background:var(--blue)}
.touch hr{position:absolute;left:92px;top:414px;width:378px;border:0;border-top:1px solid #555}
.msg{position:absolute;left:590px;top:3402px;width:610px;height:545px;background:linear-gradient(135deg,#2a9fd8,#1a85c6)}
.msg h2{position:absolute;left:32px;top:60px;color:#fff;font-weight:800;font-size:38px}
.field{position:absolute;background:#fff;border-radius:4px;font-size:15px;color:#666;padding:16px 18px}
.btn-submit{position:absolute;left:32px;top:421px;width:208px;height:52px;border-radius:26px;background:#fff;color:#333;font-weight:600;font-size:15px;display:flex;align-items:center;justify-content:center;gap:12px}
.btn-submit .dot-ico{color:var(--blue)}

/* footer */
.footer{position:absolute;left:0;top:3947px;width:1200px;height:370px;background:#fff}
.footer .brand{position:absolute;left:92px;top:120px}
.footer .social{position:absolute;left:92px;top:184px}
.footer .social span{background:#333;border:0}
.copy{position:absolute;left:92px;top:247px;font-size:14px;line-height:26px;color:#333}
.vline{position:absolute;top:68px;width:1px;height:180px;background:#ddd}
.vline:before{content:"";position:absolute;left:-1px;top:40px;width:3px;height:24px;background:var(--blue)}
.col{position:absolute;top:104px}
.col h4{font-size:18px;font-weight:700;color:#222;letter-spacing:.5px}
.col h4:after{content:"";display:block;width:34px;height:3px;background:var(--blue);margin-top:6px}
.col ul{list-style:none;font-size:15px;color:#444;line-height:30px;margin-top:8px}
.ci{display:flex;gap:14px;align-items:flex-start;font-size:15px;color:#444;line-height:26px;margin-top:14px}
.ci i{width:40px;height:40px;border-radius:50%;background:var(--blue);flex:none;display:flex;align-items:center;justify-content:center}
</style>
</head>
<body>

<header class="topbar">
  <div class="item" style="left:92px">
    <svg width="16" height="18" viewBox="0 0 16 18"><path d="M8 0a6 6 0 0 1 6 6c0 5-6 12-6 12S2 11 2 6a6 6 0 0 1 6-6z" fill="#fff"/><circle cx="8" cy="6" r="2.3" fill="#2b2c30"/></svg>
    <span><b>Address :</b> 4180 Larkspur Lane Alderton, Georgia 30091</span>
  </div>
  <div class="sep"></div>
  <div class="item" style="left:568px">
    <svg width="16" height="16" viewBox="0 0 24 24"><path d="M6.6 10.8a15 15 0 0 0 6.6 6.6l2.2-2.2a1 1 0 0 1 1-.25 11.4 11.4 0 0 0 3.6.57 1 1 0 0 1 1 1V20a1 1 0 0 1-1 1A17 17 0 0 1 3 4a1 1 0 0 1 1-1h3.5a1 1 0 0 1 1 1c0 1.25.2 2.45.57 3.57a1 1 0 0 1-.25 1z" fill="#fff"/></svg>
    <span><b>Call Us :</b> (706) 555-0147</span>
  </div>
  <div class="social"><span></span><span></span><span></span><span></span></div>
</header>

<nav class="nav">
  <div class="brand"><i></i>TRELMOND</div>
  <div class="menu">
    <a class="on">HOME</a><a>SERVICES</a><a>ROMA</a><a>MADD</a><a>RESOURCES</a>
  </div>
  <a class="btn-contact">CONTACT</a>
</nav>

<section class="hero">
  <div class="hero-photo" role="img" aria-label="Two smiling business professionals reviewing a tablet together"></div>
  <svg class="arrow" style="left:22px" width="24" height="54" viewBox="0 0 24 54"><path d="M22 2 2 27l20 25" fill="none" stroke="#888" stroke-width="2"/></svg>
  <svg class="arrow" style="left:1152px" width="24" height="54" viewBox="0 0 24 54"><path d="M2 2l20 25L2 52" fill="none" stroke="#888" stroke-width="2"/></svg>
  <h1>WELCOME TO<br><em>TRELMOND</em> GROUP</h1>
  <p>Trelmond Group, LLC was created to help nonprofits &amp; government contractors meet their basic funding..</p>
  <a class="btn-ghost">Learn More <span class="dot-ico"></span></a>
  <svg class="wave" width="1200" height="120" viewBox="0 0 1200 120" preserveAspectRatio="none">
    <path d="M0 40 C300 100 800 100 1200 20 L1200 120 L0 120Z" fill="#2a9fd8"/>
    <path d="M0 60 C300 125 800 125 1200 45 L1200 120 L0 120Z" fill="#fff"/>
  </svg>
</section>

<section class="about">
  <div class="dots" style="left:62px;top:1138px;width:12px;height:210px"></div>
  <div class="dots" style="left:62px;top:1336px;width:180px;height:12px"></div>
  <div class="about-img" role="img" aria-label="Consultant meeting with a client in a bright office"></div>
  <h2 class="h2">LEADING <span class="dot-ico" style="color:#3c3e43;width:34px;height:26px;vertical-align:middle"></span><br>ORGANIZATIONS<br>TO <em>EXCELLENCE!</em></h2>
  <p>Trelmond Group, LLC was created to help nonprofits and government contractors meet their basic funding requirements and adopt a Mission Aligned Data Driven mindset that promotes positive change in the lives of the people they serve. Our approach is not simply based off of theoretical business practices, but on practical solutions to real-life situations learned through more than twenty years of experience.</p>
</section>

<section class="services">
  <h2 class="title">OUR SERVICES</h2>
  <div class="center-ico" style="top:128px"></div>
  <div class="card" style="left:92px">
    <div class="ph" role="img" aria-label="Two consultants in suits reviewing documents" style="background:linear-gradient(135deg,#cfd3d8,#4a505a)"></div>
    <h3>Consulting</h3>
    <ul><li>General Operation<br>consulting</li><li>ROMA Implementation<br>consulting</li></ul>
  </div>
  <div class="card dark" style="left:350px">
    <div class="ph" role="img" aria-label="Trainer smiling at a laptop" style="background:linear-gradient(135deg,#e2d2b0,#c8962e)"></div>
    <h3>Training</h3>
    <ul><li>Introduction to<br>ROMA</li><li>Practical Application<br>ROMA</li></ul>
  </div>
  <div class="card" style="left:610px">
    <div class="ph" role="img" aria-label="Analyst studying charts on a monitor" style="background:linear-gradient(135deg,#1d2f4a,#b53a2a)"></div>
    <h3>Data &amp; Analytics</h3>
    <ul><li>Community Assesment<br>Development</li><li>Program Performance<br>Analysis</li></ul>
  </div>
  <div class="card" style="left:868px">
    <div class="ph" role="img" aria-label="Presenter holding a video camera" style="background:linear-gradient(135deg,#b08a68,#e6c9b4)"></div>
    <h3>Storytellinng</h3>
    <ul><li>Report<br>Development</li><li>Videography</li></ul>
  </div>
  <a class="btn-white">View All Services <span class="dot-ico"></span></a>
</section>

<section class="mission">
  <h2 class="h2">OUR <em>MISSION</em> <span class="dot-ico" style="color:#3c3e43;width:34px;height:26px"></span></h2>
  <p>To help social service organizations develop a Mission Aligned Data Driven mindset that promotes positive change in the lives of the customers they serve.</p>
  <div class="dots" style="left:502px;top:226px;width:12px;height:170px"></div>
  <div class="dots" style="left:502px;top:384px;width:150px;height:12px"></div>
  <div class="dots" style="left:1090px;top:226px;width:12px;height:170px"></div>
  <div class="dots" style="left:960px;top:384px;width:142px;height:12px"></div>
  <div class="person ceo" role="img" aria-label="Portrait of the CEO"></div>
  <div class="person cfo" role="img" aria-label="Portrait of the CFO"></div>
  <div class="caption" style="left:525px"><b>CEO</b><span>Dorian “Cal” Vesper</span></div>
  <div class="caption" style="left:815px"><b>CFO</b><span>Miriam Oakes Vesper</span></div>
</section>

<h2 class="h2 testi-title">CLIENT <em>TESTIMONIAL</em></h2>
<div class="center-ico" style="top:2906px;background:#3c3e43"></div>
<div class="tcard" style="left:92px">
  <div class="q">“</div>
  <p>It was a training, but not your typical training. It leaves you with a new and different take on things. You will find yourself saying ‘Wow, I’ve never thought of it like that before’. You will be left with new and refreshing ideas and different ways to approach situations.</p>
  <b>Marlow County Senior Services</b>
</div>
<div class="tcard" style="left:622px">
  <div class="q">“</div>
  <p>Cal is easy to work with and his expertise allows you to tailor your training to the specific needs of your agency. We highly recommend Cal and his company.</p>
  <b>Community Action Partnership<br>of Ridgeview Valley</b>
</div>
<div class="pager"><i></i><i class="on"></i><i></i></div>

<section class="touch" role="img" aria-label="Smiling consultant on a phone call, darkened">
  <h2>GET IN TOUCH <span class="dot-ico" style="color:#fff;width:34px;height:26px"></span></h2>
  <p>Trelmond Group, LLC was created for one purpose – to ensure our customers are equipped with the tools necessary to achieve excellence. We are excited to hear about your project and look forward to the opportunity to work with you.</p>
  <div class="info" style="top:348px">
    <svg width="22" height="26" viewBox="0 0 16 18"><path d="M8 0a6 6 0 0 1 6 6c0 5-6 12-6 12S2 11 2 6a6 6 0 0 1 6-6z" fill="#fff"/><circle cx="8" cy="6" r="2.3" fill="#2b2c30"/></svg>
    <span class="bar"></span><span><b style="font-weight:600">Address :</b> 4180 Larkspur Lane Alderton,<br>Georgia 30091</span>
  </div>
  <hr>
  <div class="info" style="top:444px;align-items:center">
    <svg width="22" height="22" viewBox="0 0 24 24"><path d="M6.6 10.8a15 15 0 0 0 6.6 6.6l2.2-2.2a1 1 0 0 1 1-.25 11.4 11.4 0 0 0 3.6.57 1 1 0 0 1 1 1V20a1 1 0 0 1-1 1A17 17 0 0 1 3 4a1 1 0 0 1 1-1h3.5a1 1 0 0 1 1 1c0 1.25.2 2.45.57 3.57a1 1 0 0 1-.25 1z" fill="#fff"/></svg>
    <span class="bar" style="height:30px"></span><span><b style="font-weight:600">Phone:</b> (706) 555-0147</span>
  </div>
</section>

<section class="msg">
  <h2>SEND US A MESSAGE</h2>
  <div class="field" style="left:32px;top:137px;width:237px;height:52px">Name *</div>
  <div class="field" style="left:279px;top:137px;width:237px;height:52px">Email *</div>
  <div class="field" style="left:32px;top:203px;width:484px;height:52px">Select One
    <svg style="position:absolute;right:18px;top:22px" width="12" height="8" viewBox="0 0 12 8"><path d="M0 0h12L6 8z" fill="#555"/></svg></div>
  <div class="field" style="left:32px;top:268px;width:484px;height:138px">Message *</div>
  <a class="btn-submit">Submit Now <span class="dot-ico"></span></a>
</section>

<footer class="footer">
  <div class="brand"><i></i>TRELMOND</div>
  <div class="social"><span></span><span></span><span></span><span></span></div>
  <div class="copy">Copyright © 2022 Trelmond Group.<br>All rights reserved.</div>
  <div class="vline" style="left:361px"></div>
  <div class="vline" style="left:574px"></div>
  <div class="vline" style="left:793px"></div>
  <div class="col" style="left:404px;top:110px"><h4>QUICK LINKS</h4><ul><li>Home</li><li>Services</li><li>Roma</li><li>Maad</li><li>Contact</li></ul></div>
  <div class="col" style="left:617px;top:110px"><h4>OTHERS LINK</h4><ul><li>Privacy Policy</li><li>Terms &amp; Condition</li><li>About Us</li><li>FAQ</li><li>Resources</li></ul></div>
  <div class="col" style="left:836px;top:110px"><h4>CONTACT INFO</h4>
    <div class="ci"><i><svg width="14" height="16" viewBox="0 0 16 18"><path d="M8 0a6 6 0 0 1 6 6c0 5-6 12-6 12S2 11 2 6a6 6 0 0 1 6-6z" fill="#fff"/><circle cx="8" cy="6" r="2.3" fill="#2a9fd8"/></svg></i><span>4180 Larkspur Lane Alderton,<br>Georgia 30091</span></div>
    <div class="ci" style="align-items:center"><i><svg width="16" height="16" viewBox="0 0 24 24"><path d="M6.6 10.8a15 15 0 0 0 6.6 6.6l2.2-2.2a1 1 0 0 1 1-.25 11.4 11.4 0 0 0 3.6.57 1 1 0 0 1 1 1V20a1 1 0 0 1-1 1A17 17 0 0 1 3 4a1 1 0 0 1 1-1h3.5a1 1 0 0 1 1 1c0 1.25.2 2.45.57 3.57a1 1 0 0 1-.25 1z" fill="#fff"/></svg></i><span>(706) 555-0147</span></div>
  </div>
</footer>

</body>
</html>
```